Chirper Bootstrap Website Design (Gaming Themed)

I need a website designed using Chirper Bootstrap for a Rewards website. We'd like to see a gaming based design as the site will cater mostly to gamers.
This is a rewards site similar to sites like LootPebble
I only need the HTML/CSS design.
I need these pages:
1. Homepage for non-logged in users which will also have a sign up form
2. Homepage for logged in users
3. Profile Page
4. Rewards page which will display items that the user can redeem
a) A drop-down to sort by item category
5. Rewards page item details which will display a single item's details
6. About, FAQ, Terms Of Service Pages
Reason: Waiting for some more designs
Target Market(s)
13 to 30 year old gamers
Mostly males
Industry/Entity Type
It Service
Look and feel
Each slider illustrates characteristics of the customer's brand and the style your logo design should communicate.

```html
<!DOCTYPE html>
<html lang="en">
<head>
<meta charset="utf-8">
<title>PlayQuest – Where Your Gamer Rep Lives</title>
<link href="https://fonts.googleapis.com/css2?family=Lato:wght@300;400;700;900&family=Open+Sans:wght@400;600;700&family=Kaushan+Script&display=swap" rel="stylesheet">
<style>
  :root{
    --yellow:#f2d21a;
    --yellow-dark:#d9a90a;
    --cyan:#2ee6e0;
    --white:#ffffff;
    --footer-band:#3a3a3a;
    --footer-body:#444444;
    --footer-link:#b5b5b5;
    --footer-rule:#555555;
    --social-blue:#1d5fb8;
    --field:#e3e3e3;
  }
  *{box-sizing:border-box;margin:0;padding:0}
  html,body{width:1200px;height:856px;overflow:hidden;background:var(--footer-body);font-family:'Lato',sans-serif}
  .page{position:relative;width:1200px;height:856px}

  .topbar{position:absolute;left:0;top:0;width:1200px;height:44px;background:linear-gradient(#ffffff,#e9e9e9);border-bottom:1px solid #cfcfcf}
  .brand{position:absolute;left:200px;top:8px;font:900 24px/28px 'Lato',sans-serif;color:#1f6e8c;display:flex;align-items:center;gap:6px}
  .brand .dot{width:12px;height:12px;background:#1f6e8c;border-radius:50%}
  .login{position:absolute;left:938px;top:10px;width:63px;height:25px;background:linear-gradient(#ffe23a,var(--yellow-dark));border:1px solid #b08a00;border-radius:3px;font:700 12px/23px 'Open Sans',sans-serif;color:#222;text-align:center}

  .hero{position:absolute;left:0;top:44px;width:1200px;height:635px;background:radial-gradient(ellipse at 30% 40%,#5a4a3e 0%,#3e3a3c 40%,#2a3040 75%,#3a2a24 100%)}
  .headline{position:absolute;left:200px;top:180px;width:490px;font-size:78px;line-height:64px;letter-spacing:-3px;white-space:nowrap}
  .headline .line{display:block;transform-origin:left center}
  .headline .line-two{transform:scaleX(0.79)}
  .headline .y{color:var(--yellow);font-weight:900}
  .headline .c{color:var(--cyan);font-weight:300}
  .headline .w{color:var(--white);font-weight:900}
  .tagline{position:absolute;left:196px;top:326px;width:498px;text-align:center;font:900 27px/31.5px 'Lato',sans-serif;color:var(--white);letter-spacing:-0.5px}
  .tagline .y{color:var(--yellow)}
  .how{position:absolute;left:547px;top:498px;font:400 21px/26px 'Kaushan Script',cursive;color:var(--yellow)}
  .flow{position:absolute;left:0;top:0}

  .signup{position:absolute;left:734px;top:187px;width:267px}
  .social{display:flex;height:39px;background:linear-gradient(#2a74d0,var(--social-blue));border:1px solid #124a96;border-radius:3px;color:var(--white);font:400 16px/37px 'Lato',sans-serif;white-space:nowrap;overflow:hidden}
  .social .mark{flex:0 0 52px;border-right:1px solid #124a96;display:flex;align-items:center;justify-content:center}
  .social .mark span{width:14px;height:14px;background:var(--white)}
  .social .label{padding-left:12px}
  .field{position:relative;height:35px;background:var(--field);border:1px solid #bdbdbd;border-radius:3px;margin-top:14px;font:400 15px/33px 'Lato',sans-serif;color:#8a8a8a;padding-left:16px}
  .field.active{border-color:#3a7fd8;color:#3a7fd8;margin-top:27px}
  .field .icon{position:absolute;right:0;top:0;width:34px;height:33px;border-left:1px solid #bdbdbd;display:flex;align-items:center;justify-content:center}
  .cta{margin-top:27px;height:37px;background:linear-gradient(#ffe834,var(--yellow-dark));border-radius:3px;text-align:center;font:400 21px/37px 'Lato',sans-serif;color:#1a1a1a}

  .footer-band{position:absolute;left:0;top:679px;width:1200px;height:31px;background:var(--footer-band)}
  .footer-cols{position:absolute;left:0;top:679px;width:1200px}
  .col{position:absolute;top:0}
  .col h3{height:31px;font:700 14px/31px 'Open Sans',sans-serif;color:var(--white)}
  .col ul{list-style:none;margin-top:3px;padding-left:2px}
  .col li{font:400 10px/16px Arial,sans-serif;color:var(--footer-link);letter-spacing:0.3px}
  .sep{position:absolute;top:679px;width:1px;height:31px;background:#4a4a4a}
  .rule{position:absolute;left:0;top:824px;width:1200px;height:1px;background:var(--footer-rule)}
  .copy{position:absolute;left:0;top:833px;width:1200px;text-align:center;font:400 10px/12px Arial,sans-serif;color:#6a6a6a}
</style>
</head>
<body>
<div class="page">
  <header class="topbar">
    <div class="brand"><span class="dot"></span>PlayQuest</div>
    <div class="login">LOGIN</div>
  </header>

  <section class="hero" role="img" aria-label="Dark fantasy illustration of an armoured warrior with a hammer in a burning landscape"></section>

  <h1 class="headline">
    <span class="line"><span class="y">WHERE</span> <span class="c">YOUR</span></span>
    <span class="line line-two"><span class="c">GAMER</span> <span class="w">REP</span> <span class="y">LIVES</span></span>
  </h1>
  <p class="tagline"><span class="y">PLAY &amp; TALK</span> ABOUT GAMES WITH OUR COMMUNITY OF 13 MILLION GAMERS AND EARN COOL <span class="y">REWARDS.</span></p>

  <div class="how">How It Works</div>
  <svg class="flow" width="1200" height="856" viewBox="0 0 1200 856">
    <path d="M624 406 C700 380 760 430 740 500 C725 545 690 558 652 566" fill="none" stroke="#ffffff" stroke-width="1.2" stroke-dasharray="4 3"/>
    <path d="M658 560 L650 567 L659 574" fill="none" stroke="#ffffff" stroke-width="1.2"/>
    <circle cx="600" cy="570" r="36" fill="#d8d8d8" stroke="#9a9a9a" stroke-width="2"/>
    <path d="M593 557 L613 570 L593 583 Z" fill="#2a2a2a"/>
  </svg>

  <form class="signup">
    <div class="social"><div class="mark"><span></span></div><div class="label">Sign Up with Friendspace</div></div>
    <div class="field active">Email
      <div class="icon"><svg width="18" height="18" viewBox="0 0 18 18"><circle cx="9" cy="5" r="4" fill="#1d6ed6"/><path d="M1 17 C2 11 16 11 17 17 Z" fill="#1d6ed6"/></svg></div>
    </div>
    <div class="field">Password
      <div class="icon"><svg width="14" height="18" viewBox="0 0 14 18"><path d="M3 8 V5 a4 4 0 0 1 8 0 V8" fill="none" stroke="#8a8a8a" stroke-width="2"/><rect x="1" y="8" width="12" height="9" rx="1" fill="#8a8a8a"/></svg></div>
    </div>
    <div class="cta">Free! Get Started</div>
  </form>

  <div class="footer-band"></div>
  <div class="sep" style="left:310px"></div>
  <div class="sep" style="left:459px"></div>
  <div class="sep" style="left:591px"></div>
  <div class="sep" style="left:711px"></div>
  <div class="sep" style="left:855px"></div>
  <nav class="footer-cols">
    <div class="col" style="left:200px"><h3>GamingSite</h3><ul><li>Home</li><li>About Us</li><li>Services</li><li>Rewards</li><li>FAQs</li><li>Contact Us</li></ul></div>
    <div class="col" style="left:344px"><h3>Ways to Earn</h3><ul><li>Shop</li><li>Search</li><li>Watch</li><li>Play</li><li>Answer</li><li>Credit Card</li></ul></div>
    <div class="col" style="left:491px"><h3>Rewards</h3><ul><li>Rewards Store</li><li>PlayQuest Takes</li></ul></div>
    <div class="col" style="left:627px"><h3>Connect</h3><ul><li>Friendspace</li><li>Chirper</li><li>ClipStream</li><li>Circles +</li></ul></div>
    <div class="col" style="left:746px"><h3>Information</h3><ul><li>Help Center</li><li>How it works</li><li>Winning tips</li><li>Sitemap</li></ul></div>
    <div class="col" style="left:890px"><h3>Support</h3><ul><li>Contact Us</li><li>Bussiness Development</li><li>Privacy Policy</li><li>Terms &amp; Conditions</li></ul></div>
  </nav>
  <div class="rule"></div>
  <div class="copy">© 2013 PlayQuest All Right Reserved</div>
</div>
</body>
</html>
```